Tanning Lotion package label & Logo

Need hot new label for tanning lotion focusing on dark tanning. Sexy design must compete with soon to be dated but still popular "Mabel in the jar" styles here:
http://www.shopvelder.example/s/ref=nb_sb_noss_1?url=search-alias%3Daps&field-keywords=tanning%20lotion&sprefix=tanni%2Caps&rh=i%3Aaps%2Ck%3Atanning%20lotion
Have 30 days to complete. High end product needs right look.
Product name: SunMostGlo
Target Market(s)
SunMostGlo is a high-end, one-of-a-kind, multi-purpose hybrid tanning lotion that can be used indoors as a self-tanner, outdoors on the beach, or at tanning salons. The SunMostGlo formula delivers a high performing silicone base to provide an excellent, non-irritating, non-oily, non-tacky, luxurious, light and greaseless overall feel on the skin when applied. This high performing silicon base also provides sebum absorption and control to help clear and prevent breakouts. SunMostGlo contains a complex mixture of moisturizers and emollients including vitamin B5 to prevent and treat dry skin, protect sensitive skin, and improve skin tone and texture. It also contains a powerful blend of antioxidants including Grape Seed extract which is rich in OPC’s and has 20 times the antioxidant power of vitamin C, and 50 times the antioxidant power of vitamin E to help fight free radicals, protect and improve skin appearance and maintain healthy looking skin. SunMostGlo contains a unique combination of two natural skin-tanning compounds to produce an even, deeper, and longer lasting tan. Tanning accelerators using natural amino acids help increase the production of melanin for a quicker and darker tan. SunMostGlo is the most technologically advanced tanning lotion on the market today!
SunMostGlo is a high-end product and will have a retail price point around $50 USD for 200 ml.
SunMostGlo is aimed at the mid to high market
Target demographic are white girls and women aged 16-49, followed by white males aged 18-55.
SunMostGlo will be sold online direct to consumers initially then followed by;
1. On shelves in beach area shops
2. In tanning salons
3. On shelves in mid-large box retail stores
Industry/Entity Type
Product
Look and feel

```html
<!DOCTYPE html>
<html lang="en">
<head>
<meta charset="utf-8">
<title>SunMostGlo – Advanced Tanning Lotion Label</title>
<link rel="stylesheet" href="https://fonts.googleapis.com/css2?family=Great+Vibes&family=Cinzel:wght@600&family=Josefin+Sans:wght@400&family=Oswald:wght@500&family=Berkshire+Swash&display=swap">
<style>
  :root {
    --bg-light: #f4f4f4;
    --bg-dark: #d9d9d9;
    --gold-light: #f8dc8a;
    --gold-mid: #d9a534;
    --gold-deep: #8f5a12;
    --gold-shadow: #5a3406;
    --black: #0d0d0d;
    --panel: #1b1b1b;
    --red-light: #d8262c;
    --red-deep: #7e0b10;
    --white: #ffffff;
    --ribbon-ink: #6b1a0c;
  }
  html, body {
    margin: 0;
    width: 1200px;
    height: 857px;
    overflow: hidden;
  }
  body {
    background: radial-gradient(ellipse at center, var(--bg-light) 0%, var(--bg-dark) 100%);
  }
  .label {
    display: block;
    width: 1200px;
    height: 857px;
  }
  .brand-name {
    font-family: "Great Vibes", cursive;
    font-size: 92px;
    fill: var(--white);
  }
  .product-line {
    font-family: "Josefin Sans", sans-serif;
    font-size: 21px;
    letter-spacing: 0.5px;
    fill: var(--white);
  }
  .ribbon-claim {
    font-family: "Cinzel", serif;
    font-weight: 600;
    font-size: 27px;
    fill: var(--white);
  }
  .ribbon-side-text {
    font-family: "Berkshire Swash", cursive;
    font-size: 26px;
    fill: var(--ribbon-ink);
  }
  .seal-figure {
    font-family: "Oswald", sans-serif;
    font-weight: 500;
    font-size: 46px;
    fill: var(--white);
  }
</style>
</head>
<body>
<svg class="label" viewBox="0 0 1200 857" xmlns="http://www.w3.org/2000/svg">
  <defs>
    <linearGradient id="gold" x1="0" y1="0" x2="0" y2="1">
      <stop offset="0" stop-color="var(--gold-light)"/>
      <stop offset="0.45" stop-color="var(--gold-mid)"/>
      <stop offset="1" stop-color="var(--gold-deep)"/>
    </linearGradient>
    <linearGradient id="gold-side" x1="0" y1="0" x2="1" y2="0">
      <stop offset="0" stop-color="var(--gold-deep)"/>
      <stop offset="0.5" stop-color="var(--gold-light)"/>
      <stop offset="1" stop-color="var(--gold-deep)"/>
    </linearGradient>
    <radialGradient id="gold-soft" cx="0.5" cy="0.4" r="0.7">
      <stop offset="0" stop-color="var(--gold-light)"/>
      <stop offset="0.6" stop-color="var(--gold-mid)"/>
      <stop offset="1" stop-color="var(--gold-deep)"/>
    </radialGradient>
    <linearGradient id="red" x1="0" y1="0" x2="0" y2="1">
      <stop offset="0" stop-color="var(--red-light)"/>
      <stop offset="1" stop-color="var(--red-deep)"/>
    </linearGradient>
    <radialGradient id="oval-shine" cx="0.5" cy="0.55" r="0.6">
      <stop offset="0" stop-color="#3a3a3a"/>
      <stop offset="1" stop-color="var(--black)"/>
    </radialGradient>
    <path id="claim-arc" d="M420,580 Q600,512 790,580"/>
  </defs>

  <!-- upper ornament area -->
  <path class="ornament-upper" role="img" aria-label="Gold acanthus leaf scrollwork crest"
        fill="url(#gold-soft)" stroke="var(--gold-shadow)" stroke-width="2"
        d="M125,320 Q125,160 330,145 Q490,135 545,85 Q600,50 655,85 Q710,135 870,145 Q1075,160 1075,320 Z"/>

  <!-- lower ornament area -->
  <rect class="ornament-lower" role="img" aria-label="Gold acanthus leaf scrollwork base"
        x="158" y="600" width="884" height="195" rx="60"
        fill="url(#gold-soft)" stroke="var(--gold-shadow)" stroke-width="2"/>

  <!-- rectangular frame -->
  <rect class="frame-outer" x="168" y="330" width="864" height="338" fill="url(#gold)" stroke="var(--black)" stroke-width="5"/>
  <rect class="frame-inner" x="186" y="348" width="828" height="302" fill="var(--panel)" stroke="var(--gold-shadow)" stroke-width="3"/>
  <rect class="frame-inset" x="200" y="362" width="800" height="274" fill="none" stroke="var(--gold-mid)" stroke-width="2"/>

  <!-- central oval -->
  <ellipse class="oval-rim" cx="600" cy="395" rx="282" ry="168" fill="url(#gold)" stroke="var(--black)" stroke-width="5"/>
  <ellipse class="oval-field" cx="600" cy="395" rx="262" ry="150" fill="url(#oval-shine)" stroke="var(--gold-shadow)" stroke-width="3"/>

  <!-- shield with crown -->
  <path class="shield" fill="var(--black)" stroke="url(#gold)" stroke-width="8"
        d="M540,155 L660,155 L660,215 Q660,250 600,275 Q540,250 540,215 Z"/>
  <rect class="shield-crown" role="img" aria-label="Gold crown emblem" x="570" y="185" width="60" height="40" rx="4" fill="url(#gold)"/>

  <text class="brand-name" x="600" y="408" text-anchor="middle">SunMostGlo</text>
  <text class="product-line" x="600" y="466" text-anchor="middle">ADVANCED TANNING LOTION</text>

  <!-- side ribbons -->
  <path class="ribbon-side ribbon-left" fill="url(#gold-side)" stroke="var(--gold-shadow)" stroke-width="3"
        d="M135,570 L330,520 L345,585 L150,628 L160,600 Z"/>
  <text class="ribbon-side-text" transform="translate(245,585) rotate(-13)" text-anchor="middle">your text here</text>
  <path class="ribbon-side ribbon-right" fill="url(#gold-side)" stroke="var(--gold-shadow)" stroke-width="3"
        d="M1065,570 L870,520 L855,585 L1050,628 L1040,600 Z"/>
  <text class="ribbon-side-text" transform="translate(957,585) rotate(13)" text-anchor="middle">your text here</text>

  <!-- central claim ribbon -->
  <path class="ribbon-claim-band" fill="url(#red)" stroke="url(#gold)" stroke-width="6"
        d="M385,545 Q600,470 815,545 L820,612 Q600,540 380,612 Z"/>
  <text class="ribbon-claim" text-anchor="middle"><textPath href="#claim-arc" startOffset="50%">WITH VITAMIN B, C &amp; E</textPath></text>

  <!-- seal -->
  <circle class="seal-rim" cx="600" cy="655" r="76" fill="url(#gold)" stroke="var(--black)" stroke-width="5"/>
  <circle class="seal-field" cx="600" cy="655" r="60" fill="var(--black)" stroke="var(--gold-shadow)" stroke-width="3"/>
  <text class="seal-figure" x="600" y="673" text-anchor="middle">100%</text>
</svg>
</body>
</html>
```